Small Box Design - For launch into retail market

We need artwork for small boxes that we are going to be using for the retail market. I will upload the type of box we are going to be using. The example we are uploading is of a different company that sells the same products. We would like our Logo on the box as as our web address (www.brandellgroup-ltd.com). The rest is up to you. Please contact with any questions.

Target Market(s)

Distributors, Retailers of Fasteners

Industry/Entity Type

Manufacture

Colors
0355a3
3176b5
fbee3f
fbf289

Requirements
Must have
• Our logo, our web address www.brandellgroup-ltd.com
• Somewhere on the box Washers . Stampings . Assemblies . Bearings (most likely below our logo somewhere)
Nice to have
• Blue is our corporate colour, but it's not essential. You can suggest any colours and we will consider.

```html
<!DOCTYPE html>
<html lang="en">
<head>
<meta charset="utf-8">
<title>Brandell Limited – Retail Box Dieline</title>
<link rel="stylesheet" href="https://fonts.googleapis.com/css2?family=Archivo:ital,wght@0,500;0,600;1,800&display=swap">
<style>
  :root {
    --ink-bg: #000000;
    --brand-blue: #0f56a3;
    --brand-blue-light: #2b77b5;
    --brand-yellow: #f1ec5a;
    --paper: #ffffff;
    --body-grey: #2a2a2a;
  }
  html, body {
    margin: 0;
    padding: 0;
    width: 960px;
    height: 1200px;
    overflow: hidden;
    background: var(--ink-bg);
  }
  .dieline {
    display: block;
    width: 960px;
    height: 1200px;
  }
  .panel { fill: var(--paper); }
  .band-dark { fill: var(--brand-blue); }
  .band-light { fill: var(--brand-blue-light); }
  .web-bar { fill: var(--brand-yellow); }
  .fold-line { stroke: #e4e4e4; stroke-width: 1; }
  .web-address {
    font-family: "Archivo", sans-serif;
    font-weight: 500;
    font-size: 10px;
    fill: var(--brand-blue);
    letter-spacing: 0.3px;
  }
  .product-list {
    font-family: "Archivo", sans-serif;
    font-style: italic;
    font-weight: 800;
    font-size: 10px;
    letter-spacing: 0.4px;
  }
  .product-list.on-white { fill: var(--brand-blue); }
  .product-list.on-blue { fill: var(--paper); }
  .brand-name {
    font-family: "Archivo", sans-serif;
    font-weight: 600;
    font-size: 22px;
    letter-spacing: 0.5px;
  }
  .brand-name.on-blue { fill: var(--paper); }
  .brand-name.on-white { fill: var(--brand-blue); }
  .brand-dot.on-blue { fill: var(--paper); }
  .brand-dot.on-white { fill: var(--brand-blue); }
  .body-copy {
    font-family: "Archivo", sans-serif;
    font-weight: 500;
    font-size: 8px;
  }
  .body-copy.on-blue { fill: var(--paper); }
  .body-copy.on-white { fill: var(--body-grey); }
</style>
</head>
<body>
<svg class="dieline" viewBox="0 0 1200 1500" xmlns="http://www.w3.org/2000/svg">

  <!-- Lid with rounded dust-flap ears -->
  <g class="lid">
    <path class="panel" d="M393,93 C300,110 232,190 220,268 Q216,307 252,307 L393,307 Z"/>
    <path class="band-dark" d="M797,93 C890,110 958,190 970,268 Q974,307 938,307 L797,307 Z"/>
  </g>

  <!-- Main spine: lid top, front and back -->
  <g class="main-panel">
    <rect class="panel" x="393" y="93" width="404" height="1047"/>
    <polygon class="band-light" points="722,93 737,93 393,712 393,690"/>
    <polygon class="band-dark" points="737,93 797,93 797,410 400,1140 393,1140 393,712"/>
    <polygon class="band-light" points="797,410 797,445 420,1140 400,1140"/>
  </g>

  <!-- Left side panel -->
  <g class="side-panel side-left">
    <rect class="band-dark" x="68" y="612" width="10" height="222"/>
    <rect class="panel" x="76" y="413" width="309" height="621"/>
    <polygon class="band-light" points="135,413 148,413 76,540 76,520"/>
    <polygon class="band-dark" points="148,413 385,413 385,490 97,1034 76,1034 76,540"/>
    <polygon class="band-light" points="385,490 385,515 110,1034 97,1034"/>
    <polygon class="band-light" points="76,1034 76,1010 85,1034"/>
    <polygon class="web-bar" points="185,791 385,791 385,818 170,818"/>
  </g>

  <!-- Right side panel -->
  <g class="side-panel side-right">
    <rect class="panel" x="1112" y="612" width="10" height="222"/>
    <rect class="panel" x="805" y="413" width="309" height="621"/>
    <polygon class="band-light" points="864,413 877,413 805,540 805,520"/>
    <polygon class="band-dark" points="877,413 1114,413 1114,490 826,1034 805,1034 805,540"/>
    <polygon class="band-light" points="1114,490 1114,515 839,1034 826,1034"/>
    <polygon class="web-bar" points="914,791 1122,791 1122,818 899,818"/>
  </g>

  <!-- Bottom base panel -->
  <g class="base-panel">
    <rect class="panel" x="68" y="1140" width="1054" height="214"/>
    <line class="fold-line" x1="382" y1="1140" x2="382" y2="1354"/>
    <polygon class="band-light" points="722,1140 737,1140 610,1354 598,1354"/>
    <polygon class="band-dark" points="737,1140 1122,1140 1122,1354 610,1354"/>
  </g>

  <!-- Lid artwork (reads upside down on the flat sheet) -->
  <polygon class="web-bar" points="528,118 797,118 797,145 541,145"/>
  <text class="web-address" x="712" y="135" text-anchor="middle" transform="rotate(180 712 131)">www.brandellgroup-ltd.com</text>
  <g transform="rotate(180 505 222)">
    <circle class="brand-dot on-white" cx="418" cy="215" r="5"/>
    <text class="brand-name on-white" x="430" y="230">Brandell Limited</text>
  </g>
  <g class="product-list on-blue" text-anchor="middle">
    <text x="740" y="191" transform="rotate(180 740 187)">BEARINGS</text>
    <text x="733" y="211" transform="rotate(180 733 207)">ASSEMBLIES</text>
    <text x="738" y="231" transform="rotate(180 738 227)">STAMPINGS</text>
    <text x="741" y="251" transform="rotate(180 741 247)">WASHERS</text>
  </g>

  <!-- Front artwork -->
  <g class="front-artwork">
    <circle class="brand-dot on-blue" cx="424" cy="708" r="5"/>
    <text class="brand-name on-blue" x="436" y="716">Brandell Limited</text>
    <text class="body-copy on-blue" x="412" y="774">Lorem ipsum dolor sit amet, consectetuer</text>
    <text class="body-copy on-blue" x="412" y="784">adipiscing elit, sed diam nonummy nibh</text>
    <text class="body-copy on-blue" x="412" y="794">euismod tincidunt ut laoreet dolore magna</text>
    <text class="body-copy on-blue" x="412" y="804">aliquam erat volutpat.</text>
    <g class="product-list on-white">
      <text x="697" y="709">WASHERS</text>
      <text x="697" y="728">STAMPINGS</text>
      <text x="697" y="747">ASSEMBLIES</text>
      <text x="697" y="766">BEARINGS</text>
    </g>
  </g>

  <!-- Left side artwork -->
  <g class="side-artwork">
    <circle class="brand-dot on-blue" cx="86" cy="712" r="5"/>
    <text class="brand-name on-blue" x="97" y="720" style="font-size:19px">Brandell Limited</text>
    <g class="product-list on-white">
      <text x="299" y="709">WASHERS</text>
      <text x="299" y="728">STAMPINGS</text>
      <text x="299" y="747">ASSEMBLIES</text>
      <text x="299" y="766">BEARINGS</text>
    </g>
    <text class="web-address" x="377" y="809" text-anchor="end">www.brandellgroup-ltd.com</text>
  </g>

  <!-- Right side artwork -->
  <g class="side-artwork">
    <circle class="brand-dot on-blue" cx="817" cy="712" r="5"/>
    <text class="brand-name on-blue" x="828" y="720" style="font-size:19px">Brandell Limited</text>
    <g class="product-list on-white">
      <text x="1035" y="709">WASHERS</text>
      <text x="1035" y="728">STAMPINGS</text>
      <text x="1035" y="747">ASSEMBLIES</text>
      <text x="1035" y="766">BEARINGS</text>
    </g>
    <text class="web-address" x="1107" y="809" text-anchor="end">www.brandellgroup-ltd.com</text>
  </g>

  <!-- Base artwork (reads upside down on the flat sheet) -->
  <g transform="rotate(180 515 1280)">
    <circle class="brand-dot on-white" cx="428" cy="1273" r="5"/>
    <text class="brand-name on-white" x="440" y="1288">Brandell Limited</text>
  </g>
  <g class="body-copy on-white" text-anchor="middle">
    <text x="521" y="1201" transform="rotate(180 521 1198)">aliquam erat volutpat.</text>
    <text x="521" y="1212" transform="rotate(180 521 1209)">euismod tincidunt ut laoreet dolore magna</text>
    <text x="521" y="1223" transform="rotate(180 521 1220)">adipiscing elit, sed diam nonummy nibh</text>
    <text x="521" y="1234" transform="rotate(180 521 1231)">Lorem ipsum dolor sit amet, consectetuer</text>
  </g>
  <g class="product-list on-blue" text-anchor="middle">
    <text x="740" y="1245" transform="rotate(180 740 1241)">BEARINGS</text>
    <text x="733" y="1265" transform="rotate(180 733 1261)">ASSEMBLIES</text>
    <text x="736" y="1285" transform="rotate(180 736 1281)">STAMPINGS</text>
    <text x="740" y="1305" transform="rotate(180 740 1301)">WASHERS</text>
  </g>
</svg>
</body>
</html>
```